Small environmental consultancy needs a simple but professional web design

We are a boutique environmental consultancyand contracting business located in Margaret River in the South West of Western Australia.

We have two arms
1) Consulting which offers environmental planning, management and assessment services primarily to local government and the development industry.
2) Contracting which implements on site plans and on ground works primarily involving revegetation, bush regeneration and environmental weed control.

We need a simple yet professional web design within the wordpress platform that commmunicates professionalism, experience and technical expertise without appearing too corporate.

Something like this structure appeals:
http://tarnwick.net.au/environment-services/
or
http://www.brackleyfieldworks.com.au/index.php

(without the image gallery function)

Target Market(s)

Local Government Officers deciding on tenders;
Developers, Engineers, Town Planning consultants looking for environmental expertise

Industry/Entity Type

Business

Number of Pages Required

5+ page

Font styles to use
Sans Serif

Colors
33a6d7
9bcb3c

Requirements
Must have
• Pages required include:
• Home
• Environmental Planning and Management
• Revegetation and Regeneration Implementation (This page can mirror the Environmental Planning and Management page exactly in structure but with different text and images)
• About Us (I think that this page can be relatively simple and generic)
• Contact (I think that this page can be very simple and generic)
Nice to have
• An ability to start out basic and quicikly establish a website presence and then build in additional drop downs and pages over time.
Should not have
• It does not need a photo gallery page;
• It does not need a major amount of space dedicated to social media and blogs etc as this is not currently particularly active area for us

```html
<!DOCTYPE html>
<html lang="en">
<head>
<meta charset="utf-8">
<title>Marrinup Ecoservices</title>
<link href="https://fonts.googleapis.com/css2?family=Open+Sans:wght@400;600;700&family=Oswald:wght@400;500&display=swap" rel="stylesheet">
<style>
:root{
  --blue:#33a6d7;
  --text:#555;
  --head:#222;
  --light:#f2f2f2;
  --green:#9bcb3c;
  --footer:#1c1c1c;
  --footer-2:#111;
}
*{margin:0;padding:0;box-sizing:border-box}
html,body{width:1200px;height:2956px;overflow:hidden;background:#fff;font-family:"Open Sans",sans-serif;color:var(--text)}
.page{position:relative;width:1200px;height:2956px}
/* header */
.header{position:absolute;top:0;left:0;width:1200px;height:180px;background:#fff}
.brand{position:absolute;left:28px;top:24px;display:flex;align-items:center;gap:12px}
.brand-dot{width:64px;height:64px;border-radius:50%;background:var(--green)}
.brand-name{font-family:"Oswald",sans-serif;font-size:30px;color:var(--blue);letter-spacing:.5px;white-space:nowrap}
.callus{position:absolute;right:32px;top:12px;text-align:right;font-family:"Oswald",sans-serif;line-height:1.15}
.callus small{display:block;font-size:15px;font-weight:500;color:var(--head)}
.callus strong{font-size:30px;font-weight:500;color:var(--blue)}
.search{position:absolute;right:32px;top:86px;width:210px;height:26px;border:1px solid #ccc;font-size:12px;color:#999;padding:4px 10px}
.navbar{position:absolute;left:0;top:146px;width:1130px;height:30px;background:var(--blue);display:flex;align-items:center;padding-left:160px;gap:46px}
.navbar a{color:#fff;text-decoration:none;font-size:11px;font-weight:700;text-transform:uppercase;white-space:nowrap}
/* hero */
.hero{position:absolute;top:180px;left:0;width:1200px;height:520px;background:linear-gradient(180deg,#c9d6cf 0%,#7f9a7a 45%,#486a3c 75%,#6f8d3e 100%)}
.hero-title{position:absolute;top:220px;width:100%;text-align:center;font-family:"Oswald",sans-serif;color:#fff;line-height:1.05}
.hero-title span{display:block;font-size:40px;font-weight:500;letter-spacing:1px}
.hero-title em{display:block;font-style:normal;font-size:38px;font-weight:400}
.arrow{position:absolute;top:240px;width:44px;height:44px;border-radius:50%;background:#fff;display:flex;align-items:center;justify-content:center}
.arrow.left{left:24px}.arrow.right{right:24px}
.hero-wave{position:absolute;left:0;top:620px;width:1200px}
/* features */
.drops{position:absolute;top:580px;left:0;width:1200px;display:flex;justify-content:space-around;padding:0 60px}
.drop{width:190px;height:190px;border-radius:0 50% 50% 50%;transform:rotate(45deg);border:5px solid #fff;box-shadow:0 2px 6px rgba(0,0,0,.25)}
.d1{background:radial-gradient(circle,#e4473a,#6e8b38)}
.d2{background:radial-gradient(circle,#e9754b,#5e7e3a)}
.d3{background:radial-gradient(circle,#c4432c,#9fb77f)}
.d4{background:radial-gradient(circle,#c35ca6,#6c8a49)}
.features{position:absolute;top:885px;left:70px;width:1060px;display:flex;gap:50px}
.feature{flex:1}
.feature h3{font-family:"Oswald",sans-serif;color:var(--blue);font-size:26px;font-weight:500;margin-bottom:10px}
.feature p{font-size:13px;line-height:1.5;margin-bottom:18px}
.btn{display:inline-block;background:var(--blue);color:#fff;font-size:11px;font-weight:600;padding:5px 14px;text-transform:uppercase}
/* welcome */
.welcome{position:absolute;top:1120px;left:0;width:1200px;height:520px}
.welcome-img{position:absolute;right:0;top:0;width:720px;height:520px;background:radial-gradient(ellipse at 55% 45%,#9fd2c9 0%,#cfe6d2 35%,#fff 75%)}
.welcome-text{position:absolute;left:70px;top:50px;width:500px}
.welcome-text small{font-family:"Oswald",sans-serif;color:var(--green);font-size:26px;display:block}
.welcome-text h2{font-family:"Oswald",sans-serif;color:var(--green);font-size:52px;font-weight:500;line-height:1;margin-bottom:26px}
.welcome-text p{font-size:13px;line-height:1.6;margin-bottom:16px}
.btn.green{background:var(--green)}
/* testimonials & why */
.section-title{font-family:"Oswald",sans-serif;font-size:20px;color:var(--head);font-weight:500;text-transform:uppercase}
.testimonials{position:absolute;top:1660px;left:70px;width:520px}
.testi-box{margin-top:28px;background:var(--light);padding:22px}
.quote{background:#fff;padding:22px;margin-bottom:22px}
.quote:last-child{margin-bottom:0}
.quote p{font-size:13px;line-height:1.55;font-style:italic}
.quote .who{font-size:11px;font-weight:700;margin:16px 0 8px;text-transform:uppercase;color:var(--head)}
.stars{color:#f0b323;font-size:20px;letter-spacing:2px}
.stars span{color:#ccc}
.why{position:absolute;top:1660px;left:610px;width:530px}
.why-list{position:relative;margin-top:28px}
.why-line{position:absolute;left:40px;top:40px;width:2px;height:390px;background:var(--blue)}
.why-item{position:relative;display:flex;align-items:center;height:150px}
.why-icon{width:84px;height:84px;border-radius:50%;background:var(--blue);border:4px solid #fff;box-shadow:0 0 0 2px var(--blue);display:flex;align-items:center;justify-content:center;z-index:1;flex:none}
.why-card{margin-left:-10px;flex:1;border:2px solid var(--blue);padding:14px 18px 14px 28px;background:#fff}
.why-card h4{font-size:12px;font-weight:700;color:var(--head);text-transform:uppercase;margin-bottom:6px}
.why-card p{font-size:12px;line-height:1.5}
/* projects */
.projects{position:absolute;top:2420px;left:70px;width:1060px}
.projects .section-title{text-align:center;margin-bottom:20px}
.project-row{display:flex;gap:20px}
.project{flex:1}
.project-img{height:160px;margin-bottom:12px}
.p1{background:linear-gradient(135deg,#f3c6d6,#d85c8a 55%,#7aa24a)}
.p2{background:linear-gradient(180deg,#8fb9dd,#3f6e34 55%,#87a64a)}
.p3{background:linear-gradient(180deg,#b9d6a4,#2f6a2a 60%,#4f8d33)}
.p4{background:linear-gradient(135deg,#8a7cc7,#4f3d93 50%,#6b8a3f)}
.project h5{font-family:"Oswald",sans-serif;font-size:15px;font-weight:500;color:var(--head);text-transform:uppercase;margin-bottom:4px}
.project p{font-size:12px;line-height:1.45}
/* footer */
.footer{position:absolute;top:2790px;left:0;width:1200px;height:166px;background:var(--footer);color:#ddd}
.footer-contact{display:flex;justify-content:center;align-items:center;gap:70px;height:70px;font-size:13px}
.footer-mark{width:42px;height:42px;border-radius:50%;background:var(--green)}
.footer-nav{display:flex;justify-content:center;gap:46px;height:56px;align-items:center;border-top:1px solid #333;font-size:11px;font-weight:600;text-transform:uppercase}
.footer-copy{background:var(--footer-2);height:40px;line-height:40px;text-align:center;font-size:10px;color:#888}
</style>
</head>
<body>
<div class="page">
  <header class="header">
    <div class="brand"><span class="brand-dot"></span><span class="brand-name">Marrinup Ecoservices</span></div>
    <div class="callus"><small>Call Us</small><strong>1.888.555.0142</strong></div>
    <div class="search">Search</div>
    <nav class="navbar">
      <a>Home</a><a>Environmental Planning and Management</a><a>Revegetation and Regeneration Implementation</a><a>About Us</a><a>Contact</a>
    </nav>
  </header>

  <section class="hero" role="img" aria-label="Sunlit forest with tall trees and a green meadow">
    <div class="arrow left"><svg width="16" height="16" viewBox="0 0 16 16"><path d="M11 2 5 8l6 6" stroke="#333" stroke-width="2.5" fill="none"/></svg></div>
    <div class="arrow right"><svg width="16" height="16" viewBox="0 0 16 16"><path d="M5 2l6 6-6 6" stroke="#333" stroke-width="2.5" fill="none"/></svg></div>
    <h1 class="hero-title"><span>MARRINUP ECOSERVICES</span><em>ENVIRONMENTAL CONSULTANTS</em></h1>
  </section>
  <svg class="hero-wave" width="1200" height="80" viewBox="0 0 1200 80"><path d="M0 60 Q600 -20 1200 60 L1200 80 L0 80Z" fill="#fff"/></svg>

  <div class="drops">
    <div class="drop d1" role="img" aria-label="Red flowers"></div>
    <div class="drop d2" role="img" aria-label="Orange blossom"></div>
    <div class="drop d3" role="img" aria-label="Red berries"></div>
    <div class="drop d4" role="img" aria-label="Purple thistle"></div>
  </div>

  <section class="features">
    <div class="feature"><h3>ABOUT US</h3><p>Lorem ipsum dolor sit amet, consectetur adipiscing elit, sed do eiusmod tempor incididunt ut labore et dolore magna aliqua.</p><span class="btn">Read more</span></div>
    <div class="feature"><h3>WHY US?</h3><p>Lorem ipsum dolor sit amet, consectetur adipiscing elit, sed do eiusmod tempor incididunt ut labore et dolore magna aliqua.</p><span class="btn">Read more</span></div>
    <div class="feature"><h3>CURRENT PROJECT</h3><p>Lorem ipsum dolor sit amet, consectetur adipiscing elit, sed do eiusmod tempor incididunt ut labore et dolore magna aliqua.</p><span class="btn">Read more</span></div>
    <div class="feature"><h3>CONTACT US</h3><p>Lorem ipsum dolor sit amet, consectetur adipiscing elit, sed do eiusmod tempor incididunt ut labore et dolore magna aliqua.</p><span class="btn">Read more</span></div>
  </section>

  <section class="welcome">
    <div class="welcome-img" role="img" aria-label="Hand holding a glass globe with a seedling"></div>
    <div class="welcome-text">
      <small>Welcome to</small>
      <h2>MARRINUP ECOSERVICES</h2>
      <p>Lorem ipsum dolor sit amet, consectetuer adipiscing elit, sed diam nonummy nibh euismod tincidunt ut laoreet dolore magna aliquam erat volutpat. Ut wisi enim ad minim veniam, quis nostrud exerci tation ullamcorper suscipit lobortis nisl ut aliquip ex ea commodo consequat.</p>
      <p>Lorem ipsum dolor sit amet, consectetuer adipiscing elit, sed diam nonummy nibh euismod tincidunt ut laoreet dolore magna aliquam erat volutpat. Ut wisi enim ad minim veniam, quis nostrud exerci tation ullamcorper suscipit lobortis nisl ut aliquip ex ea commodo consequat.</p>
      <span class="btn green">Read more</span>
    </div>
  </section>

  <section class="testimonials">
    <h3 class="section-title">Client's Testimonials</h3>
    <div class="testi-box">
      <div class="quote">
        <p>"Lorem ipsum dolor sit amet, consectetuer adipiscing elit, sed diam nonummy nibh euismod tincidunt ut laoreet dolore magna aliquam erat volutpat. Ut wisi enim ad minim veniam, quis nostrud exerci tation ullamcorper suscipit lobortis nisl ut aliquip ex ea commodo consequat."</p>
        <div class="who">- Dale Morven</div>
        <div class="stars">★★★<span>★★</span></div>
      </div>
      <div class="quote">
        <p>"Lorem ipsum dolor sit amet, consectetuer adipiscing elit, sed diam nonummy nibh euismod tincidunt ut laoreet dolore magna aliquam erat volutpat. Ut wisi enim ad minim veniam, quis nostrud exerci tation ullamcorper suscipit lobortis nisl ut aliquip ex ea commodo consequat."</p>
        <div class="who">- Rena Holt</div>
        <div class="stars">★★★<span>★★</span></div>
      </div>
    </div>
  </section>

  <section class="why">
    <h3 class="section-title">Why Us?</h3>
    <div class="why-list">
      <div class="why-line"></div>
      <div class="why-item">
        <div class="why-icon"><svg width="40" height="40" viewBox="0 0 40 40"><path d="M8 32C8 14 20 8 34 6c-2 16-10 26-26 26Z" fill="#fff"/><path d="M8 32 24 16" stroke="#33a6d7" stroke-width="2"/></svg></div>
        <div class="why-card"><h4>Lorem ipsum dolor sit amet</h4><p>Lorem ipsum dolor sit amet, consectetuer adipiscing elit, sed diam nonummy nibh euismod tincidunt ut laoreet dolore magna aliquam erat.</p></div>
      </div>
      <div class="why-item">
        <div class="why-icon"><svg width="40" height="40" viewBox="0 0 40 40" fill="none" stroke="#fff" stroke-width="2.5"><circle cx="20" cy="20" r="15"/><ellipse cx="20" cy="20" rx="7" ry="15"/><path d="M5 20h30M8 12h24M8 28h24"/></svg></div>
        <div class="why-card"><h4>Lorem ipsum dolor sit amet</h4><p>Lorem ipsum dolor sit amet, consectetuer adipiscing elit, sed diam nonummy nibh euismod tincidunt ut laoreet dolore magna aliquam erat.</p></div>
      </div>
      <div class="why-item">
        <div class="why-icon"><svg width="40" height="40" viewBox="0 0 40 40" fill="#fff"><rect x="18.5" y="4" width="3" height="32"/><path d="M10 9h18l5 4-5 4H10Z"/><path d="M30 20H12l-5 4 5 4h18Z"/></svg></div>
        <div class="why-card"><h4>Lorem ipsum dolor sit amet</h4><p>Lorem ipsum dolor sit amet, consectetuer adipiscing elit, sed diam nonummy nibh euismod tincidunt ut laoreet dolore magna aliquam erat.</p></div>
      </div>
    </div>
  </section>

  <section class="projects">
    <h3 class="section-title">Recent Projects</h3>
    <div class="project-row">
      <div class="project"><div class="project-img p1" role="img" aria-label="Pink blossom in spring"></div><h5>Lorem ipsum dolor sit</h5><p>Lorem ipsum dolor sit amet, consectetur adipiscing elit, sed do eiusmod tempor incididunt ut labore.</p></div>
      <div class="project"><div class="project-img p2" role="img" aria-label="Green hillside landscape"></div><h5>Lorem ipsum dolor sit</h5><p>Lorem ipsum dolor sit amet, consectetur adipiscing elit, sed do eiusmod tempor incididunt ut labore.</p></div>
      <div class="project"><div class="project-img p3" role="img" aria-label="Bright green forest"></div><h5>Lorem ipsum dolor sit</h5><p>Lorem ipsum dolor sit amet, consectetur adipiscing elit, sed do eiusmod tempor incididunt ut labore.</p></div>
      <div class="project"><div class="project-img p4" role="img" aria-label="Purple wisteria flowers"></div><h5>Lorem ipsum dolor sit</h5><p>Lorem ipsum dolor sit amet, consectetur adipiscing elit, sed do eiusmod tempor incididunt ut labore.</p></div>
    </div>
  </section>

  <footer class="footer">
    <div class="footer-contact">
      <span>(808) 555 01 2290</span>
      <span class="footer-mark"></span>
      <span>info@marrinupeco.com</span>
    </div>
    <nav class="footer-nav">
      <span>Home</span><span>Environmental Planning &amp; Management</span><span>Revegetation &amp; Regeneration Implementation</span><span>About Us</span><span>Contact</span>
    </nav>
    <div class="footer-copy">© 2015 Marrinup Ecoservices. All Rights Reserved.</div>
  </footer>
</div>
</body>
</html>
```